Boutique and Spa website design

We need a website for a new business named "Velvet Orchid Boutique and Spa" Base in the state of New York. We sell clothes and accessories as well as spa services:. Microdermabrasion,Peels,Facials,Waxing,Body treatments,.Nails: manicures and pedicures, and massage. We do not sell clothes and accessories on line. I am looking for a spa website.I want this website ready to go. I would like it in HTML/CSS. format.

Target Market(s)

ages 25 to 60

Industry/Entity Type

Business

Font styles to use
Decorative
Script

Colors

Designer to choose colors to be used in the design.

Requirements
Must have
• I want my spa services, my hours, pictures of women getting services (not the pictures below) ,and my logo listed on the website. My hours are Monday and Sunday-Closed and Tues-Friday 10-8....We offer Facials,Microdermabration,Peels,Waxing,eyebrow and eyelash tint, Eyelash extensions, manicure and pedicure, Gel nail polish and shellac,and Massage....Also sell retail skincare products, and women's name brand cloths and accessories...
Nice to have
• Maybe relaxing color tones- browns/purples/greens ....No carton pictures
Should not have
• Prices

```html
<!DOCTYPE html>
<html lang="en">
<head>
<meta charset="utf-8">
<title>Velvet Orchid Boutique and Spa</title>
<link href="https://fonts.googleapis.com/css2?family=PT+Sans:ital,wght@0,400;0,700;1,700&display=swap" rel="stylesheet">
<style>
:root{
  --purple:#9a5cc9;
  --purple-deep:#8a4fc0;
  --ink:#3a3a3a;
  --body:#4a4a4a;
  --muted:#8a8a8a;
  --rule:#d8d8d8;
  --btn-top:#6d737b;
  --btn-bottom:#4d535b;
  --footer:#464646;
  --white:#ffffff;
}
*{margin:0;padding:0;box-sizing:border-box}
html,body{width:1075px;height:1200px;overflow:hidden;background:var(--white)}
body{position:relative;font-family:Arial,Helvetica,sans-serif;color:var(--body)}
.abs{position:absolute}

/* header */
.site-header{position:absolute;left:0;top:0;width:1075px;height:80px;border-bottom:1px solid #d6d6d6;background:var(--white)}
.brand{position:absolute;left:154px;top:22px;display:flex;align-items:center;gap:8px;font-family:"PT Sans",sans-serif;font-weight:700;color:var(--purple-deep);font-size:15px;line-height:17px}
.brand-dot{width:26px;height:26px;border-radius:50%;background:var(--purple)}
.main-nav a{position:absolute;top:30px;height:24px;line-height:24px;font-size:11px;color:#555;text-decoration:none;transform:translateX(-50%)}
.main-nav a.active{left:502px;width:71px;text-align:center;background:var(--purple);color:var(--white);border-radius:2px}

/* hero */
.hero{position:absolute;left:0;top:80px;width:1075px;height:416px;
  background:radial-gradient(circle at 12% 18%,#fffbe8 0,#fbe9a8 22%,transparent 48%),
             radial-gradient(ellipse at 66% 55%,#f2c8a0 0,#e9b07c 28%,transparent 55%),
             linear-gradient(100deg,#f8e49a 0%,#f5d47a 35%,#f1c27a 60%,#e9c48a 80%,#f3dfb2 100%)}
.hero-title{position:absolute;right:627px;top:112px;font-family:"PT Sans",sans-serif;font-style:italic;font-weight:700;font-size:39px;color:var(--purple);white-space:nowrap}
.hero-text{position:absolute;right:629px;top:168px;width:340px;text-align:right;font-family:"PT Sans",sans-serif;font-weight:700;font-size:13px;line-height:24px;color:#3b3426}
.hero-btn{position:absolute;left:286px;top:341px;width:158px;height:42px;border:1px solid #b9b9b9;border-radius:2px;background:linear-gradient(#f1f1f3,#d9dade);font-family:"PT Sans",sans-serif;font-size:15px;color:#555;text-align:center;line-height:40px}
.hero-arrow{position:absolute;top:268px;width:44px;height:44px}

/* services */
.service{position:absolute;top:532px;width:235px;text-align:center}
.service-photo{width:235px;height:138px}
.service h2{margin-top:15px;font-family:"PT Sans",sans-serif;font-weight:400;font-size:17px;color:var(--purple)}
.service p{margin-top:9px;font-size:10px;line-height:18.5px;color:var(--body)}
.btn{display:block;width:99px;height:30px;line-height:28px;border:1px solid #3f444a;border-radius:2px;background:linear-gradient(var(--btn-top),var(--btn-bottom));color:var(--white);font-size:10.5px;text-align:center}
.service .btn{margin:12px 0 0 60px}
.divider{position:absolute;left:154px;top:843px;width:768px;height:1px;background:var(--rule)}

/* about */
.about-portrait{position:absolute;left:158px;top:878px}
.section-title{position:absolute;top:884px;font-family:"PT Sans",sans-serif;font-weight:700;font-size:19px;color:var(--purple)}
.about-text{position:absolute;left:377px;top:920px;width:250px;font-size:9.8px;line-height:17.6px}
.about .btn{position:absolute;left:377px;top:1026px}

/* testimonial */
.quote-mark{position:absolute;font-family:Georgia,serif;font-style:italic;font-size:34px;color:#9a9a9a;line-height:1}
.testimonial-text{position:absolute;left:686px;top:932px;width:230px;font-style:italic;font-size:9.8px;line-height:17.6px;color:#555}
.client-photo{position:absolute;left:678px;top:1017px;width:57px;height:51px;border:1px solid #ddd;background:linear-gradient(#d9c3b4,#7a5646)}
.client-name{position:absolute;left:745px;top:1027px;font-style:italic;font-size:10.5px;color:var(--purple)}
.client-date{position:absolute;left:745px;top:1043px;font-style:italic;font-size:10px;color:var(--muted)}

/* footer */
.site-footer{position:absolute;left:0;top:1120px;width:1075px;height:80px;background:var(--footer);color:#f0f0f0;font-size:10px}
.footer-nav{position:absolute;left:156px;top:25px;white-space:nowrap}
.footer-nav span.sep{margin:0 17px}
.copyright{position:absolute;left:156px;top:48px}
.social{position:absolute;top:29px;width:24px;height:24px;border-radius:50%}
</style>
</head>
<body>

<header class="site-header">
  <div class="brand"><span class="brand-dot"></span><span>Velvet Orchid<br>Boutique and Spa</span></div>
  <nav class="main-nav">
    <a class="active" href="#">Home</a>
    <a href="#" style="left:590px">About Us</a>
    <a href="#" style="left:682px">Services</a>
    <a href="#" style="left:782px">Testimonials</a>
    <a href="#" style="left:886px">Contact us</a>
  </nav>
</header>

<section class="hero" role="img" aria-label="Smiling woman with glowing skin framed by soft autumn leaves">
  <h1 class="hero-title">Velvet Orchid</h1>
  <p class="hero-text">Microdermabrasion,Peels,Facials,Waxing,Body treatments,.Nails: manicures and pedicures, and massage are our services.</p>
  <div class="hero-btn">More Services</div>
  <svg class="hero-arrow" style="left:56px" viewBox="0 0 44 44" aria-hidden="true"><circle cx="22" cy="22" r="20" fill="none" stroke="#fff" stroke-opacity=".35" stroke-width="2"/><path d="M26 13 L16 22 L26 31" fill="none" stroke="#fff" stroke-opacity=".35" stroke-width="3"/></svg>
  <svg class="hero-arrow" style="left:962px" viewBox="0 0 44 44" aria-hidden="true"><circle cx="22" cy="22" r="20" fill="none" stroke="#fff" stroke-opacity=".7" stroke-width="2"/><path d="M16 12 L30 22 L16 32 Z" fill="#fff" fill-opacity=".75"/></svg>
</section>

<article class="service" style="left:154px">
  <div class="service-photo" role="img" aria-label="Woman receiving a peel treatment with a white mask" style="background:linear-gradient(120deg,#f4efe9,#e8d7c8 55%,#e9b06a)"></div>
  <h2>Peel</h2>
  <p>Many desktop publishing packages and web page editors now use Lorem Ipsum as their default model uncover many web sites still infancy.</p>
  <span class="btn">Read more</span>
</article>
<article class="service" style="left:420px">
  <div class="service-photo" role="img" aria-label="Woman relaxing during a facial massage with spa stones and orchids" style="background:linear-gradient(120deg,#b9a48f,#d8b9a0 50%,#8c7563)"></div>
  <h2>Facials</h2>
  <p>Many desktop publishing packages and web page editors now use Lorem Ipsum as their default model uncover many web sites still infancy.</p>
  <span class="btn">Read more</span>
</article>
<article class="service" style="left:687px">
  <div class="service-photo" role="img" aria-label="Woman in a head towel receiving microdermabrasion" style="background:linear-gradient(120deg,#f2f2f2,#e6d3c7 55%,#f4f4f4)"></div>
  <h2>Microderm Abrasion</h2>
  <p>Many desktop publishing packages and web page editors now use Lorem Ipsum as their default model uncover many web sites still infancy.</p>
  <span class="btn">Read more</span>
</article>

<div class="divider"></div>

<section class="about">
  <svg class="about-portrait" width="196" height="202" viewBox="0 0 196 202" role="img" aria-label="Portrait of the spa owner">
    <circle cx="98" cy="100" r="96" fill="#fff" stroke="#e6e6e6" stroke-width="1.5"/>
    <path d="M3 104 A96 96 0 0 1 193 104" fill="none" stroke="var(--purple)" stroke-width="4"/>
    <defs><radialGradient id="portraitTone" cx="50%" cy="45%" r="55%"><stop offset="0" stop-color="#d8b79f"/><stop offset=".6" stop-color="#b08b67"/><stop offset="1" stop-color="#6e5a4a"/></radialGradient></defs>
    <circle cx="98" cy="103" r="88" fill="url(#portraitTone)"/>
  </svg>
  <h2 class="section-title" style="left:377px">About Me</h2>
  <p class="about-text">Many desktop publishing packages and web page editors now use Lorem Ipsum as their default model text, and a search for 'lorem ipsum' will uncover many web sites still in their infancy. Various versions have evolved over the years, sometimes by accident, sometimes on purpose...</p>
  <span class="btn">Read more</span>
</section>

<section class="testimonials">
  <h2 class="section-title" style="left:662px">Happy Clients</h2>
  <svg class="abs" style="left:902px;top:892px" width="22" height="10" viewBox="0 0 22 10" aria-hidden="true"><path d="M5 1 L1 5 L5 9M17 1 L21 5 L17 9" fill="none" stroke="#aaa" stroke-width="1.3"/></svg>
  <span class="quote-mark" style="left:658px;top:922px">&ldquo;</span>
  <p class="testimonial-text">Many desktop publishing packages and web page editors now use Lorem Ipsum as their default model text, and a search for 'lorem ipsum' will uncover many web sites still in their infancy...</p>
  <span class="quote-mark" style="left:902px;top:992px">&rdquo;</span>
  <div class="client-photo" role="img" aria-label="Client portrait"></div>
  <span class="client-name">Lena Marsh</span>
  <span class="client-date">24 Feb 2014</span>
</section>

<footer class="site-footer">
  <div class="footer-nav">Home<span class="sep">|</span>About Us<span class="sep">|</span>Services<span class="sep">|</span>Testimonials<span class="sep">|</span>Contact us</div>
  <div class="copyright">&copy; Copyright Velvet Orchid 2014.</div>
  <span class="social" style="left:777px;background:#3b6fb6" aria-label="Social link"></span>
  <span class="social" style="left:806px;background:#3fa9e0" aria-label="Social link"></span>
  <span class="social" style="left:837px;background:#1f7fa8" aria-label="Social link"></span>
  <span class="social" style="left:866px;background:#d9262f" aria-label="Social link"></span>
  <span class="social" style="left:897px;background:#f0a524" aria-label="Feed link"></span>
</footer>

</body>
</html>
```